Verdanix Medical Business Card

Create a high class Business card for Medical Aesthetics and Wellness Practice called Verdanix Medical Aesthetics and Wellness as per the logo attached.
Addresss is: 418 Harlan Brook Road Suite 312 Melville, New York 11093
Phone (555)204-7391 IG @verdanix_medical
Verdanixmedical.example

I need 5 different name configurations
1) Dr. Theo Valcourt
Aesthetics and Wellness Specialist
Medical Director

2) Rosalind Pettinger, NP
Clinical Nurse Manager

3) Marla Vostrik, RN
Aesthetic Nurse Specialist

4) Petra Halvesen, RN

5) Dana Kowbeck, L.E.
Senior Licensed Esthetician

Target Market(s)

22-55 Females

Industry/Entity Type

Medical Spa and Wellness

Contact Information for Business Card

Logo, address, phone, web, instagram, providers name

Requirements
Must have
• Attractive classy modern look

```html
<!DOCTYPE html>
<html lang="en">
<head>
<meta charset="utf-8">
<title>Verdanix Medical – Business Card</title>
<link href="https://fonts.googleapis.com/css2?family=Cormorant+Garamond:wght@400;500&family=Cinzel:wght@400&family=Lato:wght@400;700;900&display=swap" rel="stylesheet">
<style>
  :root {
    --bg: #8f8f8f;
    --teal-light: #22809a;
    --teal-dark: #124c5d;
    --aqua: #6cc6cb;
    --aqua-soft: #8fd3d6;
    --navy-teal: #0f4a5c;
    --ink: #222;
    --white: #fff;
  }
  * { margin: 0; padding: 0; box-sizing: border-box; }
  html, body { width: 1200px; height: 1000px; overflow: hidden; }
  body { background: var(--bg); position: relative; font-family: "Lato", sans-serif; }

  .card { position: absolute; left: 185px; width: 828px; height: 473px; border-radius: 22px; overflow: hidden; }

  /* Front */
  .card-front { top: 19px; background: radial-gradient(ellipse at 50% 22%, var(--teal-light) 0%, #1a6b82 45%, var(--teal-dark) 100%); }
  .front-illustration { position: absolute; left: 280px; top: 86px; width: 268px; height: 172px; border-radius: 14px;
    background: radial-gradient(ellipse at 50% 50%, rgba(143,211,214,.28), rgba(143,211,214,.06)); }
  .front-brand { position: absolute; left: 0; right: 0; top: 266px; text-align: center; font-family: "Cormorant Garamond", serif;
    font-weight: 400; font-size: 56px; letter-spacing: 4px; color: var(--aqua); line-height: 1; }
  .front-tagline { position: absolute; left: 0; right: 0; top: 345px; text-align: center; font-family: "Cinzel", serif;
    font-size: 16.5px; color: var(--aqua-soft); letter-spacing: .3px; }
  .front-city { position: absolute; left: 0; right: 0; top: 377px; text-align: center; font-family: "Cinzel", serif;
    font-size: 11px; letter-spacing: 5px; color: var(--aqua-soft); }

  /* Back */
  .card-back { top: 503px; background: var(--white); }
  .social { position: absolute; left: 560px; top: 30px; display: flex; align-items: center; gap: 8px; font-size: 20px; color: var(--ink); }
  .social-mark { width: 30px; height: 30px; border-radius: 6px; background: var(--aqua); }
  .divider-shadow { position: absolute; left: 448px; top: 115px; width: 60px; height: 340px;
    background: radial-gradient(ellipse at 0% 50%, rgba(0,0,0,.16), rgba(0,0,0,0) 70%); }

  .identity { position: absolute; left: 0; width: 460px; top: 140px; text-align: center; }
  .back-brand { font-family: "Cormorant Garamond", serif; font-size: 40px; letter-spacing: 3px; color: var(--navy-teal); line-height: 1; }
  .back-tagline { font-family: "Cinzel", serif; font-size: 12.5px; color: var(--navy-teal); margin-top: 12px; }
  .back-city { font-family: "Cinzel", serif; font-size: 8.5px; letter-spacing: 4px; color: var(--navy-teal); margin-top: 6px; }
  .person-name { font-weight: 900; font-size: 33px; color: var(--navy-teal); margin-top: 38px; letter-spacing: .3px; }
  .person-title { font-size: 19px; color: var(--ink); margin-top: 14px; line-height: 1.22; }
  .person-role { font-weight: 700; }

  .contact { position: absolute; left: 500px; width: 290px; top: 170px; text-align: center; color: var(--ink); font-size: 23px; }
  .contact-icons { display: flex; justify-content: center; align-items: center; gap: 8px; margin-bottom: 30px; }
  .contact-icons .rule { width: 26px; height: 2px; background: var(--aqua); }
  .contact-icons svg { width: 26px; height: 26px; }
  .contact p { margin-bottom: 17px; }
  .address { line-height: 1.15; }
</style>
</head>
<body>
  <section class="card card-front">
    <div class="front-illustration" role="img" aria-label="Line illustration of a relaxed woman at a spa with candles, stones, rolled towel and flower"></div>
    <div class="front-brand">verdanix</div>
    <div class="front-tagline">MEDICAL AESTHETICS AND WELLNESS</div>
    <div class="front-city">NEW YORK</div>
  </section>

  <section class="card card-back">
    <div class="social"><span class="social-mark"></span><span>@verdanix_medical</span></div>
    <div class="divider-shadow"></div>

    <div class="identity">
      <div class="back-brand">verdanix</div>
      <div class="back-tagline">MEDICAL AESTHETICS AND WELLNESS</div>
      <div class="back-city">NEW YORK</div>
      <div class="person-name">DR. THEO VALCOURT</div>
      <div class="person-title">Aesthetics and Wellness Specialist<br><span class="person-role">Medical Director</span></div>
    </div>

    <div class="contact">
      <div class="contact-icons">
        <span class="rule"></span>
        <svg viewBox="0 0 26 26" fill="none" stroke="#6cc6cb" stroke-width="1.8"><rect x="1" y="1" width="24" height="24" rx="4"/><rect x="9" y="6" width="8" height="14" rx="1.5"/><line x1="12" y1="17.5" x2="14" y2="17.5"/></svg>
        <svg viewBox="0 0 26 26" fill="none" stroke="#6cc6cb" stroke-width="1.8" stroke-linejoin="round"><rect x="1" y="1" width="24" height="24" rx="4"/><path d="M6 13 L20 7 L16 20 L12 15 Z"/><path d="M12 15 L20 7"/></svg>
        <svg viewBox="0 0 26 26" fill="none" stroke="#6cc6cb" stroke-width="1.8"><rect x="1" y="1" width="24" height="24" rx="4"/><path d="M13 21 C9 16 8 13.5 8 11.5 a5 5 0 0 1 10 0 C18 13.5 17 16 13 21 Z"/><circle cx="13" cy="11.5" r="1.8"/></svg>
        <span class="rule"></span>
      </div>
      <p>(555)204-7391</p>
      <p>Verdanixmedical.example</p>
      <p class="address">418 Harlan Brook Road<br>Suite 312 Melville,<br>New York 11093</p>
    </div>
  </section>
</body>
</html>
```